Website Wordpress Responsive Design and Development - Landscape Company

Site is currently under construction, but the old site needs a refresh.
Need a fully responsive wordpress website (built in Elementor or comparable theme).
Here's the way it looked prior :
https://pastpages.example/snap/20220330041341/http://brookmoorgreens.example/
Their current designer came up with a website sample and it looks terrible :
https://talkowenpics.sitebuild.example/mysite/projects
Websites the client likes for some inspiration, but needs better than these :
https://www.quarrinbeckgroundworkers.example/
http://kvatelierpx.example/
https://tullidgepartners.example/
https://www.garbettcoinc.example/

Navigation includes :
• Home
• Complete structure of website content is available in the home page, yielding main information on services.
• Visually appealing but simple to use and navigate. Subtle amount of content, but enough for search engines to be able to read up the target phrases.
• Sections on the home page include :
▪ About - Information about the company and main service focus
▪ Gallery - Imagery categorized to include lightbox style zoom.
▪ Contact - Contact details and connection information
• About
• Bannered header
• Content appropriately formatted to subject
• Gallery
• Bannered header
• Each of the albums would have their own categorized image content
• Contact
• Bannered header
• Social Media connector available on all pages (like box, feed, etc) if applicable
• Content can be updated on all pages
• Basic Optimization for SEO with title tags, meta data where applicable.
• Google Analytics and Sitemap installed. (google account will be provided)
• Google Business Listing and Search Console Accounts created

Coded - Design and coding required

1 page

• Wordpress Responsive Design

```html
<!DOCTYPE html>
<html lang="en">
<head>
<meta charset="utf-8">
<title>Brookmoor Greens – Landscape Construction &amp; Maintenance</title>
<link rel="stylesheet" href="https://fonts.googleapis.com/css2?family=Outfit:wght@500;600&family=Open+Sans:wdth,wght@75..100,300..700&display=swap">
<style>
:root{
  --green:#2a5a0c;
  --green-dark:#234e09;
  --ink:#1b1b1b;
  --muted:#8a8a8a;
  --line:#d9d9d9;
  --field:#fafafa;
  --white:#ffffff;
}
*{box-sizing:border-box;margin:0;padding:0}
html,body{width:1200px;height:2430px;overflow:hidden;background:var(--white)}
body{position:relative;font-family:"Open Sans",sans-serif;font-stretch:80%;color:var(--ink)}
.abs{position:absolute}
.heading{font-family:"Outfit",sans-serif;font-weight:600;color:var(--green)}
.btn{position:absolute;background:var(--green);color:var(--white);font-weight:700;font-size:17px;display:flex;align-items:center;justify-content:center;font-stretch:75%}

/* hero */
.hero{left:0;top:0;width:1200px;height:640px;overflow:hidden}
.hero-photo{position:absolute;inset:0;background:linear-gradient(180deg,#c9d6ea 0%,#efe6de 35%,#f3e3cf 55%,#9fb483 72%,#7fae4f 85%,#8cbc5a 100%)}
.hero-sheen{position:absolute;inset:0}
.site-header{left:0;top:0;width:1200px;height:115px;border-bottom:1px solid #6d6d6d}
.follow{left:142px;top:23px;font-size:17px;font-weight:600;display:flex;align-items:center;gap:10px}
.social-dot{width:12px;height:12px;border-radius:50%;background:var(--green);display:inline-block}
.brand-top{left:0;width:1200px;top:14px;text-align:center;font-size:35px}
.book{left:940px;top:20px;width:100px;height:38px}
.nav{top:75px;font-size:19px}
.nav.active{color:#3f7a1d}
.welcome{left:0;width:1200px;top:220px;text-align:center;font-family:"Outfit",sans-serif;font-weight:600;font-size:33px;color:var(--ink)}
.hero-title{left:0;width:1200px;top:254px;text-align:center;font-size:56px;line-height:68px}
.hero-text{left:320px;width:560px;top:332px;text-align:center;font-size:18px;line-height:27px}
.start{left:543px;top:399px;width:112px;height:38px}
.dots{left:582px;top:596px;display:flex;gap:4px}
.dots span{width:6px;height:6px;border-radius:50%;background:#fff;border:1px solid #fff}
.dots span:first-child{background:transparent}

/* about */
.section-title{font-size:40px}
.underline{height:3px;width:36px;background:var(--green)}
.about-text{left:143px;top:808px;width:500px;font-size:20px;line-height:32px;font-weight:400;font-stretch:82%}
.about-photo{left:681px;top:712px;width:370px;height:352px;background:linear-gradient(180deg,#8fb2de 0%,#cddcef 30%,#c9a07d 48%,#9b6b45 62%,#6e8c4a 80%,#6fae3a 100%)}

/* gallery */
.gallery{left:0;top:1195px;width:1200px;height:434px;display:grid;grid-template-columns:297px 301px 301px 301px;grid-template-rows:217px 217px}

/* contact form */
.field{position:absolute;background:var(--field);border-bottom:1px solid var(--line);box-shadow:0 0 2px rgba(0,0,0,.08);font-size:15px;color:var(--muted);padding:12px 17px}
.footer-col h3{font-size:22px;margin-bottom:10px}
.footer-col li{list-style:none;font-size:18px;height:36px}
.footer-text{left:142px;top:2222px;width:340px;font-size:17.5px;line-height:27.5px;font-stretch:84%}
.footer-bar{left:0;top:2390px;width:1200px;height:40px;background:var(--green-dark);color:var(--white);font-size:13px;display:flex;align-items:center;justify-content:center;font-weight:600}
</style>
</head>
<body>

<!-- hero with header -->
<section class="abs hero">
  <div class="hero-photo" role="img" aria-label="Sunlit golf course with sand bunkers, trees and houses in the distance"></div>
  <svg class="hero-sheen" width="1200" height="640" viewBox="0 0 1200 640">
    <polygon points="0,0 180,0 0,640" fill="#ffffff" opacity=".35"/>
    <polygon points="1200,90 1200,640 1034,640" fill="#ffffff" opacity=".3"/>
    <polygon points="180,0 1200,0 1200,90 1034,640 0,640" fill="#ffffff" opacity=".18"/>
    <polyline points="342,285 287,285 287,421 543,421" fill="none" stroke="#2a5a0c" stroke-width="4"/>
    <polyline points="858,285 913,285 913,421 655,421" fill="none" stroke="#2a5a0c" stroke-width="4"/>
    <polyline points="80,333 72,341 80,349" fill="none" stroke="#2a5a0c" stroke-width="3"/>
    <polyline points="1131,333 1139,341 1131,349" fill="none" stroke="#2a5a0c" stroke-width="3"/>
  </svg>

  <header class="abs site-header">
    <div class="abs follow">Follow us :
      <span class="social-dot"></span><span class="social-dot"></span><span class="social-dot"></span>
    </div>
    <div class="abs heading brand-top">Brookmoor Greens</div>
    <a class="btn book">Book Now</a>
    <nav>
      <span class="abs nav active" style="left:433px">Home</span>
      <span class="abs nav" style="left:526px">About</span>
      <span class="abs nav" style="left:616px">Gallery</span>
      <span class="abs nav" style="left:713px">Contact</span>
    </nav>
  </header>

  <div class="abs welcome">Welcome to</div>
  <h1 class="abs heading hero-title">Brookmoor Greens</h1>
  <p class="abs hero-text">Lorem Ipsum is simply dummy text of the printing and typesetting industry. Lorem Ipsum has been the industry's standard dummy text ever since the 1500s,</p>
  <a class="btn start">Get Started</a>
  <div class="abs dots"><span></span><span></span><span></span><span></span></div>
</section>

<!-- about -->
<section>
  <h2 class="abs heading section-title" style="left:143px;top:732px">About Us</h2>
  <div class="abs underline" style="left:144px;top:780px"></div>
  <p class="abs about-text">Brookmoor Greens is a full service landscape construction and maintenance company. We have been servicing the community for over 20 years and in that time have established ourselves as a premier contractor in the Hamptons. We pride ourselves on quality work and excellent customer service.</p>
  <a class="btn" style="left:143px;top:995px;width:113px;height:39px">Read More</a>
  <svg class="abs" style="left:880px;top:690px" width="210" height="70" viewBox="0 0 210 70"><polygon points="14,0 207,0 183,70 0,70" fill="#2a5a0c"/></svg>
  <div class="abs about-photo" role="img" aria-label="Modern two-storey house with a landscaped rock and flower bed and stepping stones across the lawn"></div>
</section>

<!-- gallery -->
<section>
  <h2 class="abs heading section-title" style="left:0;width:1200px;text-align:center;top:1120px">Gallery</h2>
  <div class="abs underline" style="left:541px;top:1167px"></div>
  <div class="abs gallery">
    <div role="img" aria-label="Garden path with flowering plants beside a house" style="background:linear-gradient(160deg,#b9a68a,#6e8f3a 55%,#c25a5a)"></div>
    <div role="img" aria-label="Modern white and timber house with front lawn" style="background:linear-gradient(180deg,#8fb7e0,#d7d7d2 55%,#6f9a45)"></div>
    <div role="img" aria-label="Landscaped lawn with trees and a white garden wall" style="background:linear-gradient(180deg,#eeeeee,#7a9a5a 50%,#5fa33a)"></div>
    <div role="img" aria-label="Hand-coloured landscape garden plan with pool" style="background:linear-gradient(135deg,#e8ecd2,#b8d49a 45%,#7fb8d8 75%,#eeeeee)"></div>
    <div role="img" aria-label="Grey house at sunset with shrubs and lawn" style="background:linear-gradient(180deg,#d88a84,#5e6a7a 50%,#4f7f30)"></div>
    <div role="img" aria-label="Sunny garden lawn with trees and hedges" style="background:linear-gradient(180deg,#7fa04a,#a9c95a 50%,#5fb82a)"></div>
    <div role="img" aria-label="Architectural sketch of a landscaped site plan" style="background:linear-gradient(135deg,#f2f2f2,#d2e2c8 55%,#8cc07a)"></div>
    <div role="img" aria-label="Suburban house with trees and a green lawn" style="background:linear-gradient(180deg,#8fb6e2,#cfc5b8 45%,#5f9a35)"></div>
  </div>
</section>

<!-- contact -->
<section>
  <h2 class="abs heading section-title" style="left:0;width:1200px;text-align:center;top:1675px">Contact</h2>
  <div class="abs underline" style="left:535px;top:1722px"></div>
  <p class="abs" style="left:0;width:1200px;text-align:center;top:1737px;font-size:18px">Lorem Ipsum is simply dummy text of the printing and typesetting industry</p>
  <div class="field" style="left:283px;top:1810px;width:304px;height:44px">First Name</div>
  <div class="field" style="left:611px;top:1810px;width:305px;height:44px">Last Name</div>
  <div class="field" style="left:283px;top:1874px;width:304px;height:44px">Phone</div>
  <div class="field" style="left:611px;top:1874px;width:305px;height:44px">Email</div>
  <div class="field" style="left:283px;top:1944px;width:633px;height:72px">Message</div>
  <a class="btn" style="left:512px;top:2053px;width:176px;height:40px">Submit</a>
</section>

<!-- footer -->
<footer>
  <div class="abs heading" style="left:141px;top:2165px;font-size:34px">Brookmoor Greens</div>
  <p class="abs footer-text">Brookmoor Greens is a full service landscape construction and maintenance company. We have been servicing the community for over 20 years and in that time have established ourselves as a premier contractor in the Hamptons.</p>
  <div class="abs footer-col" style="left:537px;top:2177px">
    <h3 class="heading">Quick Links</h3>
    <ul><li>Home</li><li>About</li><li>Gallery</li><li>Contact</li></ul>
  </div>
  <div class="abs footer-col" style="left:698px;top:2177px">
    <h3 class="heading">Help Links</h3>
    <ul><li>Terms &amp; Conditions</li><li>Privacy Policy</li><li>About Us</li><li>Support</li></ul>
  </div>
  <div class="abs footer-col" style="left:900px;top:2177px">
    <h3 class="heading">Contact</h3>
  </div>
  <div class="abs" style="left:901px;top:2218px;font-size:17px;font-weight:600">Email Us:</div>
  <svg class="abs" style="left:876px;top:2248px" width="17" height="13" viewBox="0 0 17 13"><rect x="1" y="1" width="15" height="11" fill="none" stroke="#2a5a0c" stroke-width="1.4"/><polyline points="1,1 8.5,7 16,1" fill="none" stroke="#2a5a0c" stroke-width="1.4"/></svg>
  <div class="abs" style="left:902px;top:2244px;font-size:15px">info@brookmoorgreens.example</div>
  <div class="abs" style="left:902px;top:2280px;font-size:17px;font-weight:600">Call Us:</div>
  <svg class="abs" style="left:880px;top:2309px" width="14" height="14" viewBox="0 0 24 24"><path d="M6.6 10.8a15.1 15.1 0 0 0 6.6 6.6l2.2-2.2a1 1 0 0 1 1-.25 11.4 11.4 0 0 0 3.6.57 1 1 0 0 1 1 1V20a1 1 0 0 1-1 1A17 17 0 0 1 3 4a1 1 0 0 1 1-1h3.5a1 1 0 0 1 1 1c0 1.250.2 2.45.57 3.6a1 1 0 0 1-.25 1z" fill="#2a5a0c"/></svg>
  <div class="abs" style="left:903px;top:2306px;font-size:15px">+(1) 88 8888 8888</div>
  <div class="abs footer-bar">© copyrights 2022 Brookmoor Greens |&nbsp; All Rights Reserved</div>
</footer>

</body>
</html>
```